Business Card Design for Law firm - already have logo

Now that we have a logo, we need a business card design - our logo is attached -it is salaryman font if that helps - we would like a file that can be uploaded to cardquill (www.cardquill-example.com) using the logo and with the following information on it:
Quenby Law Firm, P.C.
Delwyn Quenby, Esq.
5817 SW 19th Ave.
Fernhollow, OR 97999
971.555.0142 phone
971.555.0187 fax
del@quenby-example.net
Chatline: delquenby
Talkwire: delwyn.quenby@mailbox-example.com
Target Market(s)
our business cards are distributed to corporate executives, technology professionals and healthcare providers
Industry/Entity Type
Business
Look and feel

```html
<!DOCTYPE html>
<html lang="en">
<head>
<meta charset="utf-8">
<title>Quenby Law Firm – Business Card</title>
<link rel="stylesheet" href="https://fonts.googleapis.com/css2?family=Exo+2:wght@300;400&display=swap">
<style>
  :root {
    --backdrop: #d9d9d9;
    --card-frame: #1f1f1f;
    --card-face: #f7f7f7;
    --ink: #2a2a2a;
    --ink-soft: #3a3a3a;
    --rule: #2a2a2a;
  }
  html, body {
    margin: 0;
    width: 1200px;
    height: 900px;
    overflow: hidden;
    background: var(--backdrop);
    font-family: "Exo 2", sans-serif;
  }
  .business-card {
    position: absolute;
    left: 100px;
    top: 164px;
    width: 1000px;
    height: 572px;
    background: var(--card-frame);
    box-shadow: 0 12px 30px rgba(0,0,0,0.25);
  }
  .card-face {
    position: absolute;
    inset: 30px;
    background: var(--card-face);
    color: var(--ink);
  }
  .firm-wordmark {
    position: absolute;
    left: 130px;
    top: 42px;
    display: flex;
    align-items: center;
    gap: 20px;
  }
  .wordmark-square {
    width: 44px;
    height: 44px;
    background: var(--ink);
  }
  .wordmark-name {
    font-weight: 400;
    font-size: 72px;
    letter-spacing: 16px;
    line-height: 1;
    color: var(--ink);
  }
  .attorney-name {
    position: absolute;
    left: 48px;
    top: 300px;
    font-weight: 300;
    font-size: 34px;
    letter-spacing: 2px;
    margin: 0;
  }
  .messaging {
    position: absolute;
    left: 48px;
    bottom: 38px;
    font-weight: 300;
    font-size: 22px;
    line-height: 1.3;
    color: var(--ink-soft);
  }
  .column-rule {
    position: absolute;
    left: 590px;
    top: 172px;
    width: 1.5px;
    height: 190px;
    background: var(--rule);
  }
  .contact-block {
    position: absolute;
    left: 616px;
    top: 160px;
    font-weight: 300;
    font-size: 22px;
    line-height: 1.3;
    color: var(--ink-soft);
  }
  .contact-block p { margin: 0; }
  .contact-block .firm-address { margin-top: 6px; }
</style>
</head>
<body>
  <div class="business-card">
    <div class="card-face">
      <div class="firm-wordmark">
        <span class="wordmark-square"></span>
        <span class="wordmark-name">QUENBY</span>
      </div>

      <h1 class="attorney-name">DELWYN QUENBY, ESQ.</h1>

      <div class="messaging">
        <div>Chatline: delquenby</div>
        <div>Talkwire: delwyn.quenby@mailbox-example.com</div>
      </div>

      <div class="column-rule"></div>

      <div class="contact-block">
        <p>T: 971.555.0142</p>
        <p>F: 971.555.0187</p>
        <p>E: del@quenby-example.net</p>
        <p class="firm-address">Quenby Law Firm, P.C.</p>
        <p>5817 SW 19th Ave.</p>
        <p>Fernhollow, OR 97999</p>
      </div>
    </div>
  </div>
</body>
</html>
```